依頼詳細
サイト構成・基本的な要件については
https://zumora.example/diagrams/P3TR8xmaqelu2sHb
を併せてご覧いただければ幸いです。
※導線が確保されていれば、必ずしもレイアウト案に忠実である必要はございません。
ぜひご提案いただければ幸甚です。

また、素材については
http://nibulo-share.example/download/58174a2c9d3e0b6f1a7c4e2d9b8f0a6c3e5d7b1f
よりダウンロードいただければと存じます。

上記だけで制作が難しい場合は
http://moruka.example/
などから、5000円程度までならこちらにて購入可能です。カンプデータにて作成頂き、
納品時に当方にて購入したデータに差し替えていただければと存じます。

全体的なデザインのイメージとしては

http://www.tovira-hatake.example/
http://www.samolet.example/rollmode/
http://vesmira.example/
http://ri-kogetsu.example/
のような、白ベースですっきりと見やすい印象が希望です。

メインカラーは既存サイトと同様、グリーンでお願いします。
http://www.tobakitchen.example/
サイトURL
ページ数
1ページ
希望イメージ
シンプル 複雑
単色 カラフル
暗い 明るい
日常 高級
遊び心 厳粛
未来的 伝統的
女性的 男性的
希望する色
白を基調とし、グリーンベースでスッキリと明るく見やすいデザインを希望します
納品ファイル
• 高解像度JPG (.jpg)
• フォトショップ形式 (.psd)
補足説明
素材については
よりダウンロードいただければと存じます。

上記だけで制作が難しい場合は
http://moruka.example/

白ベースでメインカラーは既存と同様にグリーンを使用し、
明るく見やすいデザインをお願いできればと思います。

http://bottom-parts.example/2012/166.html
http://bottom-parts.example/2011/115.html
→フッター部分の参照

基本レイアウト
については、必ずしも忠実である必要はありません。

是非ご提案お待ちしております。
何卒よろしくお願いいたします。

制作につきましてご不明な点がございましたら、お気軽にお申し付けいただければと存じます。
ご提案お待ちしております。

クライアント様との協議の結果こちらの案を採用させていただきました。
高級感と柔らかさのバランスがとてもよく、
視認性も高く、要望を全て満たしておりましたので
こちらの案を採用いたしました。

この度は多数ご提案いただきありがとうございました。
当選に至らなかったランサー様におかれましては大変心苦しいのですが、
またの機会にぜひご提案いただければ幸甚です。
引き続き何卒よろしくお願いいたします。

```html
<!DOCTYPE html>
<html lang="ja">
<head>
<meta charset="utf-8">
<title>トバクッキング</title>
<link href="https://fonts.googleapis.com/css2?family=Noto+Serif+JP:wght@400;600;700&family=Noto+Sans+JP:wght@400;700&family=Playfair+Display:ital,wght@1,400;1,700&display=swap" rel="stylesheet">
<style>
:root{
  --green-dark:#1d4410;
  --green:#356618;
  --green-mid:#5e8c32;
  --green-pale:#edf2e2;
  --cream:#f7f5ee;
  --line:#c9d3b8;
  --text:#3a3a30;
  --muted:#77776a;
  --yellow:#f4d21c;
  --accent:#c8581a;
  --white:#ffffff;
}
*{margin:0;padding:0;box-sizing:border-box}
html,body{width:695px;height:1200px;overflow:hidden;background:var(--white)}
body{font-family:"Noto Serif JP",serif;color:var(--text);font-size:9px;position:relative}
.page{position:absolute;inset:0;background:linear-gradient(#fff 0,#fff 262px,var(--cream) 262px)}
.ph{display:block}

/* header */
.header{position:absolute;left:0;top:0;width:695px;height:215px}
.brand{position:absolute;left:78px;top:38px;display:flex;align-items:center;gap:10px}
.brand-mark{width:26px;height:26px;border-radius:50%;background:var(--green)}
.brand-name{font-size:17px;font-weight:600;color:var(--green-dark);letter-spacing:1px;line-height:1.1}
.brand-sub{font-size:7px;letter-spacing:2px;color:var(--green-dark);display:block}
.tagline{position:absolute;left:78px;top:96px;font-size:10px;line-height:1.7;color:var(--green)}
.hero{position:absolute;left:372px;top:0;width:268px;height:212px;background:radial-gradient(circle at 45% 60%,#d0392a 0,#d6682e 22%,#8cae3f 45%,#e9efd9 80%,#fff 100%)}

/* nav */
.gnav{position:absolute;left:0;top:215px;width:695px;height:47px;background:linear-gradient(var(--green),var(--green-dark));display:flex;justify-content:center;border-top:2px solid var(--green-mid)}
.gnav a{width:95px;text-align:center;color:#fff;text-decoration:none;padding-top:6px;border-right:1px solid rgba(255,255,255,.25)}
.gnav a:first-child{border-left:1px solid rgba(255,255,255,.25)}
.gnav .en{font-family:"Playfair Display",serif;font-style:italic;font-size:15px;display:block;line-height:1.2}
.gnav .ja{font-size:7px;display:block;margin-top:2px}

/* sidebar */
.side{position:absolute;left:70px;top:290px;width:150px}
.contact{border:1px solid var(--line);background:#fff}
.contact-head{background:var(--yellow);color:var(--accent);font-weight:700;font-size:10px;text-align:center;padding:5px 0;line-height:1.3}
.contact-row{display:flex;align-items:center;padding:5px 6px;border-top:1px dotted var(--line);font-size:8px}
.contact-row .school{width:36px;color:var(--muted)}
.contact-row .tel{font-family:"Noto Sans JP",sans-serif;font-weight:700;color:var(--accent);font-size:11px}
.menu{margin-top:30px;border:1px solid var(--line);background:#fff;padding:6px}
.menu a{display:block;text-align:center;font-size:10px;color:var(--text);text-decoration:none;padding:9px 0;border:1px solid var(--green-pale);margin-bottom:4px;background:linear-gradient(#fff,var(--green-pale))}
.menu a:last-child{margin-bottom:0}
.corp{margin-top:12px;display:block;height:34px;background:var(--green-dark);color:#fff;text-decoration:none;font-size:10px;display:flex;align-items:center;justify-content:center;gap:6px}
.corp svg{width:9px;height:9px}

/* main */
.main{position:absolute;left:232px;top:290px;width:395px}
.sec-title{display:flex;align-items:baseline;gap:8px;border-bottom:1px solid var(--line);padding-bottom:3px}
.sec-title .en{font-family:"Playfair Display",serif;font-style:italic;font-size:13px;color:var(--green-dark)}
.sec-title .ja{font-size:7px;color:var(--muted)}
.topics li{list-style:none;display:flex;gap:14px;font-size:9px;padding:6px 4px;border-bottom:1px dotted var(--line)}
.topics time{color:var(--green)}
.monthly{margin-top:20px}
.monthly-list{display:flex;gap:8px;margin-top:8px}
.dish{width:93px}
.dish .ph{height:46px;background:radial-gradient(circle,#e3c9a0 0,#b07744 45%,#ece4d3 75%)}
.dish p{font-size:7px;line-height:1.4;margin-top:3px;text-align:center}
.about{margin-top:18px}
.cards{display:grid;grid-template-columns:1fr 1fr;gap:8px 10px;margin-top:8px}
.card{background:#fff;border:1px solid var(--line);height:130px;padding:5px}
.card h3{font-size:9px;font-weight:700;color:var(--green-dark);display:flex;align-items:center;gap:5px;border-bottom:1px solid var(--green-pale);padding-bottom:4px}
.card h3::before{content:"";width:6px;height:6px;background:var(--green)}
.card .ph{height:62px;margin-top:5px;background:linear-gradient(135deg,#f0e3c4,#c9a46a 50%,#f5efe0)}
.card p{font-size:7px;line-height:1.5;margin-top:4px;color:var(--muted)}
.card.feature .ph{background:linear-gradient(135deg,#f3e6b7,#d8b457 50%,#fbf3da)}
.card.sunday .ph{background:linear-gradient(135deg,#cfe4ee,#7fb0c8 50%,#eaf3f6)}

/* footer */
.footer{position:absolute;left:0;top:1005px;width:695px;height:195px;background:var(--green-dark)}
.footer-top{position:relative;height:133px;background:linear-gradient(var(--green),var(--green-dark))}
.footer-veg{position:absolute;left:55px;top:-20px;width:110px;height:110px;background:radial-gradient(circle at 50% 55%,#c8421f 0,#6f9a30 45%,rgba(53,102,24,0) 72%)}
.footer-brand{position:absolute;left:78px;top:92px;display:flex;align-items:center;gap:8px;color:#fff}
.footer-brand .brand-mark{width:18px;height:18px;background:#fff}
.footer-brand .brand-name{color:#fff;font-size:13px}
.footer-brand .brand-sub{color:#fff;font-size:6px}
.lesson{position:absolute;left:330px;top:30px;color:var(--yellow);font-size:17px;font-weight:700;line-height:1.25;text-align:center}
.lesson small{display:block;font-size:7px;color:#fff;font-weight:400;margin-top:4px}
.footer-tel{position:absolute;left:488px;top:35px;color:#fff;font-size:8px;line-height:1.9}
.footer-tel b{font-family:"Noto Sans JP",sans-serif;font-size:10px;margin-left:8px}
.footer-nav{height:40px;border-top:1px solid var(--green-mid);border-bottom:1px solid var(--green-mid);display:flex;flex-wrap:wrap;justify-content:center;align-content:center;gap:3px 16px;padding:0 120px}
.footer-nav a{color:#fff;text-decoration:none;font-size:7px}
.footer-nav a::before{content:"● ";font-size:5px}
.copy{text-align:center;color:#cfdcc0;font-size:6px;padding-top:8px;font-family:"Noto Sans JP",sans-serif}
</style>
</head>
<body>
<div class="page">
  <header class="header">
    <div class="brand">
      <span class="brand-mark"></span>
      <div class="brand-name">トバクッキング<span class="brand-sub">TOBA COOKING</span></div>
    </div>
    <p class="tagline">一人ひとりの笑顔にこだわり、<br>実践的な家庭料理から<br>本格的なおもてなし料理まで提供できます</p>
    <div class="hero ph" role="img" aria-label="色とりどりの新鮮な野菜の写真"></div>
  </header>

  <nav class="gnav">
    <a href="#"><span class="en">Home</span><span class="ja">ホーム</span></a>
    <a href="#"><span class="en">About</span><span class="ja">当校について</span></a>
    <a href="#"><span class="en">Admission</span><span class="ja">入校案内</span></a>
    <a href="#"><span class="en">Course</span><span class="ja">コース案内</span></a>
    <a href="#"><span class="en">Questions</span><span class="ja">よくあるご質問</span></a>
    <a href="#"><span class="en">Class</span><span class="ja">教室案内</span></a>
  </nav>

  <aside class="side">
    <div class="contact">
      <div class="contact-head">見学・体験レッスン<br>受付中！</div>
      <div class="contact-row"><span class="school">銀座校</span><span class="tel">03-4820-1157</span></div>
      <div class="contact-row"><span class="school">日本橋校</span><span class="tel">03-4820-1163</span></div>
      <div class="contact-row"><span class="school">柏校</span><span class="tel">04-7290-3318</span></div>
    </div>
    <nav class="menu">
      <a href="#">HOME</a>
      <a href="#">当校について</a>
      <a href="#">入会案内</a>
      <a href="#">コース案内</a>
      <a href="#">料金表</a>
      <a href="#">よくあるご質問</a>
      <a href="#">教室案内</a>
      <a href="#">お問い合わせ</a>
    </nav>
    <a class="corp" href="#">企業の皆様へ<svg viewBox="0 0 10 10"><path d="M3 1l4 4-4 4" fill="none" stroke="#fff" stroke-width="2"/></svg></a>
  </aside>

  <main class="main">
    <section>
      <div class="sec-title"><span class="en">Topics</span><span class="ja">新着情報</span></div>
      <ul class="topics">
        <li><time>2013.01.01</time>フランス料理特選講座を始めました。</li>
        <li><time>2013.01.01</time>飾り料理特選講座を始めました。</li>
        <li><time>2013.01.01</time>洋菓子料理特選講座を始めました。</li>
        <li><time>2013.01.01</time>イタリア料理特選講座を始めました。</li>
      </ul>
    </section>

    <section class="monthly">
      <div class="sec-title"><span class="en">Monthly Special</span><span class="ja">今月のメニュー紹介</span></div>
      <div class="monthly-list">
        <div class="dish"><div class="ph" role="img" aria-label="今月のメニュー料理の写真"></div><p>2013.01<br>今月のメニュー料理タイトル</p></div>
        <div class="dish"><div class="ph" role="img" aria-label="今月のメニュー料理の写真"></div><p>2013.01<br>今月のメニュー料理タイトル</p></div>
        <div class="dish"><div class="ph" role="img" aria-label="今月のメニュー料理の写真"></div><p>2013.12<br>今月のメニュー料理タイトル</p></div>
        <div class="dish"><div class="ph" role="img" aria-label="今月のメニュー料理の写真"></div><p>2013.11<br>今月のメニュー料理タイトル</p></div>
      </div>
    </section>

    <section class="about">
      <div class="sec-title"><span class="en">About</span><span class="ja">当校のコース案内</span></div>
      <div class="cards">
        <article class="card feature"><h3>トバクッキングの特徴</h3><div class="ph" role="img" aria-label="料理教室の調理風景の写真"></div><p>少人数制で一人ひとりに丁寧に指導。基礎から応用まで楽しく学べます。</p></article>
        <article class="card"><h3>レギュラーコース</h3><div class="ph" role="img" aria-label="家庭料理の写真"></div><p>入門から上級まで段階的に学べる、毎日の料理に役立つ定番コースです。</p></article>
        <article class="card"><h3>専門・特別コース</h3><div class="ph" role="img" aria-label="洋菓子の写真"></div><p>和洋中や製菓など、専門的な技術をじっくり身につけられる講座です。</p></article>
        <article class="card"><h3>短期集中コース</h3><div class="ph" role="img" aria-label="スープ料理の写真"></div><p>短い期間で基本をしっかり習得したい方におすすめのコースです。</p></article>
        <article class="card sunday"><h3>サンデーコース</h3><div class="ph" role="img" aria-label="休日の料理レッスンの写真"></div><p>お仕事が忙しい方も日曜日に無理なく通える人気のコースです。</p></article>
        <article class="card"><h3>男性コース</h3><div class="ph" role="img" aria-label="男性向け料理の写真"></div><p>初めての方でも安心。男性だけで気軽に料理を楽しめます。</p></article>
      </div>
    </section>
  </main>

  <footer class="footer">
    <div class="footer-top">
      <div class="footer-veg ph" role="img" aria-label="野菜の写真"></div>
      <div class="footer-brand">
        <span class="brand-mark"></span>
        <div class="brand-name">トバクッキング<span class="brand-sub">TOBA COOKING</span></div>
      </div>
      <p class="lesson">見学・体験レッスン<br>受付中！<small>お気軽にお問い合わせください</small></p>
      <p class="footer-tel">銀座校<b>03-4820-1157</b><br>日本橋校<b>03-4820-1163</b><br>柏校<b>04-7290-3318</b></p>
    </div>
    <nav class="footer-nav">
      <a href="#">HOME</a><a href="#">入会案内</a><a href="#">当校について</a><a href="#">コース案内</a><a href="#">料金表</a><a href="#">よくあるご質問</a>
      <a href="#">教室案内</a><a href="#">お問い合わせ</a><a href="#">サイトマップ</a><a href="#">プライバシーポリシー</a>
    </nav>
    <p class="copy">Copyright©2013 Toba Kitchen All Rights Reserved.</p>
  </footer>
</div>
</body>
</html>
```